Bref créative
Modern Creative Stationary for Tech Start up!!!
TheByteDepot - Business cards - Letterheads - Email Signature -
Use same font as used in my logo
Smaller Text can be different- but in line with theme.
Professional
Pavel Orsk
Sales & Logistics
2nd Floor Birch Court
7X Fernhill Street
Pellham
Castlebury
HBX 8QW
0208 731 XXXX
07452168XXX
pavel@thebytedepotz.com
thebytedepotz.com
We want a double sided Business card that is elegant, modern, sleek and also creative. The logo should give you an idea of where we want to go in terms of theme.
Be creative, Be sexy and try your hardest as there is plenty more work to be done after this project.
This is our Logo.
We do not really like the shaded background. So it might be best to keep it flat black.
This is the white version of our Logo. It may be an idea to use this for the stationary.

```html
<!DOCTYPE html>
<html lang="en">
<head>
<meta charset="utf-8">
<title>TheByteDepot – Business Card</title>
<link rel="stylesheet" href="https://fonts.googleapis.com/css2?family=Montserrat:wght@700&family=Raleway:wght@300;400;500&display=swap">
<style>
  :root {
    --backdrop: #23282c;
    --card: #111213;
    --band: #ffffff;
    --ink-light: #e6e6e6;
    --ink-dark: #1a1a1a;
    --accent: #2ba9e1;
    --ring: #3b9fd8;
  }
  * { margin: 0; padding: 0; box-sizing: border-box; }
  html, body {
    width: 1200px; height: 797px; overflow: hidden;
    background: var(--backdrop);
  }
  .stage {
    position: relative; width: 1200px; height: 797px;
    display: flex; justify-content: center; align-items: center; gap: 40px;
  }
  .card {
    position: relative; width: 340px; height: 560px;
    background: var(--card); border-radius: 4px;
    box-shadow: 0 12px 30px rgba(0,0,0,.45);
    overflow: hidden;
  }
  .brand {
    display: flex; align-items: center; gap: 10px;
    font-family: "Montserrat", sans-serif; font-weight: 700;
    color: var(--ink-light); letter-spacing: .5px;
  }
  .brand-mark {
    border-radius: 50%; border: 4px solid var(--ring); flex: none;
  }
  .front .brand {
    position: absolute; top: 52px; left: 0; right: 0;
    justify-content: center; font-size: 20px;
  }
  .front .brand-mark { width: 30px; height: 30px; }
  .name-band {
    position: absolute; top: 190px; left: 0;
    width: 280px; height: 58px;
    background: var(--band);
    border-radius: 0 26px 0 0;
    padding: 10px 0 0 24px;
    font-family: "Raleway", sans-serif;
  }
  .person-name { color: var(--accent); font-size: 16px; font-weight: 500; }
  .person-role { color: var(--ink-dark); font-size: 11px; margin-top: 3px; }
  .address, .contacts {
    position: absolute; right: 24px; text-align: right;
    font-family: "Raleway", sans-serif; color: var(--ink-light);
    font-size: 11.5px; font-weight: 300; font-style: normal; line-height: 1.55;
  }
  .address { top: 372px; }
  .contacts { top: 452px; }
  .contact-line { display: flex; justify-content: flex-end; align-items: center; gap: 7px; }
  .contact-icon { width: 11px; height: 11px; flex: none; }
  .web-band {
    position: absolute; top: 112px; right: 0;
    width: 270px; height: 40px;
    background: var(--band);
    border-radius: 22px 0 0 0;
    padding: 12px 0 0 32px;
    font-family: "Raleway", sans-serif; font-size: 11.5px;
    color: var(--ink-dark);
  }
  .back .brand {
    position: absolute; top: 330px; left: 0; right: 0;
    flex-direction: column; gap: 18px; font-size: 30px;
  }
  .back .brand-mark { width: 110px; height: 110px; border-width: 8px; }
</style>
</head>
<body>
<main class="stage">
  <section class="card front" aria-label="Business card front">
    <div class="brand"><span class="brand-mark"></span>TheByteDepot</div>
    <div class="name-band">
      <p class="person-name">Pavel Orsk</p>
      <p class="person-role">Sales &amp; Logistics</p>
    </div>
    <address class="address">
      2nd Floor Birch Court<br>
      7X Fernhill Street<br>
      Pellham, Castlebury, HBX 8QW
    </address>
    <div class="contacts">
      <p class="contact-line">0208 731 XXXX
        <svg class="contact-icon" viewBox="0 0 12 12"><rect width="12" height="12" rx="2" fill="var(--accent)"/><path d="M3.5 3h1.6l.6 1.6-.9.6a4 4 0 0 0 2 2l.6-.9 1.6.6V8.5C9 9 8.5 9 8 9 5.2 8.8 3.2 6.8 3 4c0-.5 0-1 .5-1z" fill="#111"/></svg>
      </p>
      <p class="contact-line">07452168XXX
        <svg class="contact-icon" viewBox="0 0 12 12"><rect x="3" y="1" width="6" height="10" rx="1" fill="none" stroke="var(--ink-light)" stroke-width="1"/><circle cx="6" cy="9.3" r=".6" fill="var(--ink-light)"/></svg>
      </p>
      <p class="contact-line">pavel@thebytedepotz.com
        <svg class="contact-icon" viewBox="0 0 12 12"><rect width="12" height="12" rx="2" fill="var(--accent)"/><path d="M2.5 4h7v4.5h-7zM2.5 4 6 6.6 9.5 4" fill="none" stroke="#111" stroke-width=".9"/></svg>
      </p>
      <p class="contact-line">thebytedepotz.com
        <svg class="contact-icon" viewBox="0 0 12 12"><circle cx="6" cy="6" r="5.5" fill="var(--accent)"/><path d="M1 6h10M6 1c-2 2.5-2 7.5 0 10M6 1c2 2.5 2 7.5 0 10" fill="none" stroke="#111" stroke-width=".8"/></svg>
      </p>
    </div>
  </section>

  <section class="card back" aria-label="Business card back">
    <div class="web-band">www.thebytedepotz.com</div>
    <div class="brand"><span class="brand-mark"></span>TheByteDepot</div>
  </section>
</main>
</body>
</html>
```